Re-design of Business Card

We require a design for our business card.

Korrim is a supplier of industrial packaging specializing in plastic products. We are undergoing a rebranding to appear more corporate. We have changed our company name to korrim and have a new logo.

I have uploaded our old card design with the previous company name.
Don't copy the current design. We are looking for a new design.

Industry/Entity Type

Manufacturing

Contact Information for Business Card

please don't copy the current design. we are looking for a new design.

Font styles to use
Sans Serif

Colors

Designer to choose colors to be used in the design.

Requirements
Must have
• clean and easy to read.

```html
<!DOCTYPE html>
<html lang="en">
<head>
<meta charset="utf-8">
<title>Korrim Business Card</title>
<link rel="stylesheet" href="https://fonts.googleapis.com/css2?family=Montserrat:wght@700&family=Ubuntu:wght@400&display=swap">
<style>
  :root {
    --backdrop: #c9bdaf;
    --card-dark: #2d2d2d;
    --card-light: #ececea;
    --accent: #d8701f;
  }
  * { margin: 0; padding: 0; box-sizing: border-box; }
  html, body { width: 1200px; height: 1200px; overflow: hidden; }
  body { background: var(--backdrop); position: relative; font-family: "Ubuntu", sans-serif; color: var(--accent); }

  .card { position: absolute; left: 66px; width: 1023px; height: 517px; }
  .card--front { top: 53px; background: var(--card-dark); }
  .card--back { top: 664px; background: var(--card-light); }

  .wordmark {
    position: absolute;
    font-family: "Montserrat", sans-serif;
    font-weight: 700;
    color: var(--accent);
    letter-spacing: 4px;
    line-height: 1;
    text-align: center;
  }
  .card--front .wordmark { left: 267px; top: 53px; width: 489px; height: 124px; font-size: 96px; line-height: 124px; }
  .card--back .wordmark { left: 51px; top: 209px; width: 382px; height: 97px; font-size: 74px; line-height: 97px; }

  .service { position: absolute; top: 286px; width: 240px; }
  .service__title { font-family: "Montserrat", sans-serif; font-weight: 700; font-size: 18px; line-height: 24px; letter-spacing: .5px; }
  .service__list { list-style: none; margin-top: 34px; font-size: 19px; line-height: 24px; }
  .service__list li { padding-left: 11px; text-indent: -11px; }
  .service__list li::before { content: ". "; }
  .service--containment { left: 48px; }
  .service--containment .service__list { margin-top: 40px; }
  .service--flexible { left: 296px; top: 289px; }
  .service--machinery { left: 541px; top: 289px; }
  .service--machinery .service__list { margin-top: 10px; }
  .service--general { left: 771px; }

  .divider { position: absolute; left: 467px; top: 69px; width: 12px; height: 355px; background: var(--accent); }

  .person { position: absolute; left: 510px; top: 66px; }
  .person__name { font-family: "Montserrat", sans-serif; font-weight: 700; font-size: 37px; line-height: 40px; letter-spacing: .5px; }
  .person__role { font-size: 21px; line-height: 24px; margin-left: 6px; letter-spacing: .3px; }

  .contacts { position: absolute; left: 508px; top: 184px; list-style: none; font-size: 25px; letter-spacing: .5px; }
  .contacts li { position: relative; padding-left: 39px; line-height: 30px; }
  .contacts svg { position: absolute; left: 0; top: 4px; width: 32px; height: 24px; fill: none; stroke: var(--accent); stroke-width: 2.4; }
  .contacts .contact--phone { margin-bottom: 13px; }
  .contacts .contact--fax { margin-bottom: 15px; }
  .contacts .contact--email { margin-bottom: 22px; }
  .contacts .contact--web { margin-bottom: 22px; }
  .contacts .contact--address { line-height: 28px; }
</style>
</head>
<body>
  <section class="card card--front">
    <div class="wordmark">KORRIM</div>

    <div class="service service--containment">
      <h2 class="service__title">Pallet containment</h2>
      <ul class="service__list"><li>Stretch</li><li>Heat shrink</li><li>Pallet hood</li></ul>
    </div>
    <div class="service service--flexible">
      <h2 class="service__title">Flexible packaging</h2>
      <ul class="service__list"><li>Bags &amp;liners</li><li>Tube</li><li>Film &amp; sheet</li><li>Printed films (12 col)</li><li>Shrink films</li></ul>
    </div>
    <div class="service service--machinery">
      <h2 class="service__title">Pallet wrapping<br>machinery</h2>
      <ul class="service__list"><li>Semi &amp; Fully Auto lines</li><li>Finance options include lease,Rent, Pay per wrap</li></ul>
    </div>
    <div class="service service--general">
      <h2 class="service__title">General packaging</h2>
    </div>
  </section>

  <section class="card card--back">
    <div class="wordmark">KORRIM</div>
    <div class="divider"></div>

    <div class="person">
      <h1 class="person__name">Dana Whitfield</h1>
      <p class="person__role">Machinery Sales Manager</p>
    </div>

    <ul class="contacts">
      <li class="contact--phone">
        <svg viewBox="0 0 32 24"><path d="M6 20c-3-3-2-7 2-12 4-5 9-7 13-5l3 2-3 4-3-2c-3 0-7 5-7 8l3 2-3 4z"/></svg>1300 555 014</li>
      <li class="contact--fax">
        <svg viewBox="0 0 32 24"><rect x="3" y="8" width="26" height="11" rx="2"/><rect x="9" y="3" width="14" height="5"/><rect x="9" y="14" width="14" height="8"/></svg>+61 735 550 188</li>
      <li class="contact--email">
        <svg viewBox="0 0 32 24"><rect x="4" y="4" width="24" height="16"/><path d="M4 4l12 10 12-10"/></svg>sales@northpackgroup.com.au</li>
      <li class="contact--web">
        <svg viewBox="0 0 32 24"><circle cx="16" cy="12" r="10"/><ellipse cx="16" cy="12" rx="4" ry="10"/><path d="M6 12h20M8 7h16M8 17h16"/></svg>www.korrim.com.au</li>
      <li class="contact--address">
        <svg viewBox="0 0 32 24"><path d="M12 22c-5-7-7-10-7-13a7 7 0 0114 0c0 3-2 6-7 13z" fill="var(--accent)" stroke="none"/><circle cx="12" cy="9" r="2.5" fill="var(--card-light)" stroke="none"/></svg>48 Harlow Rd Eastvale Hills,<br>Qld 4000 Australia</li>
    </ul>
  </section>
</body>
</html>
```